Modern web-site for a game changer new health app!

We need a very clean UX / UI design for our company website that will be used to sell our brand to large corporations and their employees. If we find a good match, we'd need you to do the app design and some graphics for ongoing design needs.

For a first of its kind app developed at Whitcombe University, making licensed holistic medicine accessible to everyday people through access and curation by democratizing holistic health.

Please read the details attached thoroughly and reach out if you have any questions. Many thanks!
Updates

I've updated our requirements to make it easier, please review new details in the PDF shared. Many thanks!

Final brief refinement just uploaded, much has been simplified with very clear guidelines, please update and apply. thanks much!

Target Market(s)

corporate employees and large C level corporate leaders

Industry/Entity Type

wellness

Number of Pages Required

4 page

Font styles to use
Other font styles liked:
• We need website design now and app and socials after, hoping the designer we choose now can work with us on a regular basis going forward

Requirements
Must have
• clean, modern, minimal rich
Nice to have
• some added touches to give a custom feel
Should not have
• pictures, natural looking images or shapes

```html
<!DOCTYPE html>
<html lang="en">
<head>
<meta charset="utf-8">
<title>ORVA — Health for Everyone</title>
<link rel="stylesheet" href="https://fonts.googleapis.com/css2?family=IBM+Plex+Mono:wght@400;600&family=Red+Hat+Display:wght@400;500;600&display=swap">
<style>
  :root{
    --ink:#1c1c1c;
    --white:#ffffff;
    --cream:#fdf4e3;
    --gold:#f6b73c;
    --gold-line:#f3c86a;
    --card-grey:#a8a8a8;
    --dark-card:#1d1a17;
    --rule:#e6e6e6;
    --muted:#777777;
  }
  *{box-sizing:border-box;margin:0;padding:0}
  html,body{width:1200px;height:2549px;overflow:hidden;background:var(--white)}
  body{position:relative;font-family:"IBM Plex Mono",monospace;color:var(--ink)}
  .abs{position:absolute}

  /* hero */
  .hero-bg{left:0;top:0;width:1200px;height:708px;
    background:radial-gradient(ellipse at 25% 30%,#4a5a44 0%,transparent 45%),
               radial-gradient(ellipse at 70% 45%,#3b5634 0%,transparent 40%),
               radial-gradient(ellipse at 85% 15%,#56604f 0%,transparent 35%),
               linear-gradient(180deg,#0f120e 0%,#1d2a19 55%,#0d0f0c 100%)}
  .cream-band{left:0;top:708px;width:1200px;height:795px;background:var(--cream)}
  .brand{left:34px;top:30px;font-family:"Red Hat Display",sans-serif;font-weight:600;font-size:19px;color:var(--white);letter-spacing:.5px}
  .nav{top:38px;left:626px;display:flex;gap:46px;font-size:11.5px;color:var(--white);letter-spacing:.6px}
  .nav .active{text-decoration:underline}
  .btn{display:inline-flex;align-items:center;justify-content:center;border-radius:21px;font-family:"IBM Plex Mono",monospace;font-size:11.5px;letter-spacing:.6px}
  .btn-gold{left:1066px;top:25px;width:109px;height:33px;background:var(--gold);color:var(--ink)}
  .btn-white{background:var(--white);color:var(--ink)}
  .btn-dark{background:var(--ink);color:var(--white)}
  .hero-title{left:0;width:1200px;top:168px;text-align:center;font-family:"Red Hat Display",sans-serif;font-weight:400;font-size:56px;letter-spacing:5px;color:var(--white)}
  .hero-sub{left:0;width:1200px;top:270px;text-align:center;font-size:18px;line-height:23.5px;color:var(--white)}
  .hero-sub b{font-weight:600}

  .feature{background:var(--card-grey);border-radius:18px;color:var(--white);font-family:"Red Hat Display",sans-serif;font-weight:500;font-size:15.5px;line-height:22.5px;text-align:center;display:flex;align-items:flex-end;justify-content:center;padding:0 12px 22px}
  .brand-card{border-radius:18px;background:linear-gradient(160deg,#d97a0c 0%,#e49a34 45%,#c98a52 100%);overflow:hidden}
  .brand-card span{position:absolute;left:0;right:0;top:14px;text-align:center;font-family:"Red Hat Display",sans-serif;font-weight:500;font-size:30px;color:var(--white);letter-spacing:2px}

  /* how it works */
  .how-title{left:100px;top:958px;font-family:"Red Hat Display",sans-serif;font-size:42px;letter-spacing:3px;font-weight:400}
  .how-copy{left:100px;top:1042px;width:420px;font-size:18px;line-height:23.5px}
  .how-copy p+p{margin-top:23.5px}
  .how-copy b{font-weight:600}
  .step{left:660px;width:440px;height:150px;border:1px solid var(--gold-line);border-radius:18px;padding:24px 0 0 50px}
  .step h3{font-family:"Red Hat Display",sans-serif;font-weight:600;font-size:17.5px;letter-spacing:1.6px;margin-bottom:14px}
  .step p{font-size:13.5px;line-height:21px}
  .step-num{width:66px;height:66px;border-radius:50%;background:var(--gold);color:var(--white);font-family:"Red Hat Display",sans-serif;font-size:30px;font-weight:500;display:flex;align-items:center;justify-content:center}

  /* comparison */
  .connector{left:600px;top:1503px;width:1px;height:96px;background:var(--gold-line)}
  .connector-dot{left:596px;top:1596px;width:8px;height:8px;border-radius:50%;background:var(--gold)}
  .compare{left:270px;top:1603px;width:660px;height:357px;border:1px solid #f5f1ea;border-radius:20px}
  .compare table{position:absolute;left:39px;top:20px;width:583px;border-collapse:collapse}
  .compare th{text-align:left;font-family:"Red Hat Display",sans-serif;font-weight:600;font-size:15.5px;letter-spacing:1.6px;height:46px;border-bottom:1px solid var(--rule);padding-left:2px}
  .compare th.others{color:var(--muted);font-weight:500}
  .compare td{font-size:11px;letter-spacing:.5px;height:57.5px;border-bottom:1px solid var(--rule);padding-left:2px}
  .compare tr:last-child td{border-bottom:none}
  .tick{display:inline-block;vertical-align:middle;margin-left:4px}

  /* coming soon */
  .soon{left:83px;top:2062px;width:1034px;height:323px;border-radius:24px;
    background:radial-gradient(ellipse at 0% 100%,#f3bd5a 0%,transparent 45%),linear-gradient(180deg,#c4901f 0%,#caa04a 60%,#d8a847 100%)}
  .soon-title{left:0;width:1200px;top:2118px;text-align:center;font-family:"Red Hat Display",sans-serif;font-size:42px;letter-spacing:4px;color:var(--white)}
  .soon-sub{left:0;width:1200px;top:2183px;text-align:center;font-size:18.5px;color:var(--white);letter-spacing:.4px}
  .perk{top:2316px;width:221px;height:149px;border-radius:18px;background:var(--dark-card);color:var(--white);font-size:12.5px;letter-spacing:.6px;text-align:center}
  .perk .check{position:absolute;left:86px;top:33px;width:50px;height:50px;border-radius:50%;background:var(--gold);display:flex;align-items:center;justify-content:center}
  .perk .label{position:absolute;left:0;right:0;top:105px}
</style>
</head>
<body>

<div class="abs hero-bg" role="img" aria-label="Dark close-up photograph of white flowers among green leaves"></div>
<div class="abs cream-band"></div>

<div class="abs brand">ORVA</div>
<nav class="abs nav">
  <span class="active">HOME</span><span>MEMBERSHIP</span><span>ORGANIZATIONS</span><span>CONTACT</span>
</nav>
<a class="abs btn btn-gold">VIEW PLANS</a>

<h1 class="abs hero-title">HEALTH FOR EVERYONE</h1>
<p class="abs hero-sub"><b>All-Inclusive Holistic Wellness</b> $25/monthly.<br>Time tested science changing the lives of<br>millions at a price everyone can afford.</p>
<a class="abs btn btn-white" style="left:546px;top:385px;width:125px;height:41px">VIEW PLANS</a>

<div class="abs feature" style="left:100px;top:378px;width:187px;height:225px">1 On 1 With Holistic Doctors &amp; Unlimited Texting</div>
<div class="abs feature" style="left:100px;top:620px;width:187px;height:183px">Personalized Custom Supplements</div>
<div class="abs feature" style="left:303px;top:495px;width:187px;height:308px">Gut, Hormone<br>&amp; Cellular Lab Tests</div>
<div class="abs brand-card" style="left:506px;top:578px;width:187px;height:225px" role="img" aria-label="Orange geometric pattern artwork with brand name"><span>ORVA</span></div>
<div class="abs feature" style="left:709px;top:495px;width:187px;height:308px">Free Yoga, Meditation<br>&amp; Health Essentials<br>By Star PRactitioners</div>
<div class="abs feature" style="left:912px;top:378px;width:187px;height:225px">Unlimited<br>Classes</div>
<div class="abs feature" style="left:912px;top:620px;width:187px;height:183px">Workshops</div>

<h2 class="abs how-title">HOW IT WORKS:</h2>
<div class="abs how-copy">
  <p><b>Sign-up</b> and get a full read of your unique constitution and what makes it thrive with a <b>custom plan made one on one with your on-demand holistic Doctor/Educator.</b></p>
  <p><b>Unlimited texting</b> to address your plan or any other concern you have about your health.</p>
</div>
<a class="abs btn btn-dark" style="left:100px;top:1295px;width:125px;height:42px">VIEW PLANS</a>

<div class="abs step" style="top:903px"><h3>TAKE TEST</h3><p>Banh lo-fi cardigan, taiyaki thundercats<br>forage pickled locavore mumblecore<br>whatever sustainable tumblr vinyl.</p></div>
<div class="abs step-num" style="left:627px;top:945px">1</div>
<div class="abs step" style="top:1078px"><h3>GET MATCHED WITH A SPECIALIST</h3><p>Banh lo-fi cardigan, taiyaki thundercats<br>forage pickled locavore mumblecore<br>whatever sustainable tumblr vinyl.</p></div>
<div class="abs step-num" style="left:627px;top:1120px">2</div>
<div class="abs step" style="top:1253px"><h3>VIDEO CONSULT</h3><p>Banh lo-fi cardigan, taiyaki thundercats<br>forage pickled locavore mumblecore<br>whatever sustainable tumblr vinyl.</p></div>
<div class="abs step-num" style="left:627px;top:1295px">3</div>

<div class="abs connector"></div>
<div class="abs connector-dot"></div>
<div class="abs compare">
  <table>
    <tr><th style="width:265px">HOLLISTIC</th><th style="width:176px">ORVA</th><th class="others">OTHERS</th></tr>
    <tr><td>QUALIFIED PHD</td><td>FREE<svg class="tick" width="10" height="8" viewBox="0 0 10 8"><path d="M1 4l3 3 5-6" fill="none" stroke="#f6b73c" stroke-width="1.6"/></svg></td><td>$400 OUR OF POCKET</td></tr>
    <tr><td>1 ON 1</td><td>FREE<svg class="tick" width="10" height="8" viewBox="0 0 10 8"><path d="M1 4l3 3 5-6" fill="none" stroke="#f6b73c" stroke-width="1.6"/></svg></td><td>$400 OUR OF POCKET</td></tr>
    <tr><td>PERSONALIZED</td><td>FREE<svg class="tick" width="10" height="8" viewBox="0 0 10 8"><path d="M1 4l3 3 5-6" fill="none" stroke="#f6b73c" stroke-width="1.6"/></svg></td><td>WEARABLES</td></tr>
    <tr><td>TIME TESTED</td><td>FREE<svg class="tick" width="10" height="8" viewBox="0 0 10 8"><path d="M1 4l3 3 5-6" fill="none" stroke="#f6b73c" stroke-width="1.6"/></svg></td><td>SUPPLEMENT MARKETERS</td></tr>
    <tr><td>WESTERN &amp; EASTERN</td><td>FREE<svg class="tick" width="10" height="8" viewBox="0 0 10 8"><path d="M1 4l3 3 5-6" fill="none" stroke="#f6b73c" stroke-width="1.6"/></svg></td><td>N/A</td></tr>
  </table>
</div>

<div class="abs soon" role="img" aria-label="Golden geometric pattern background"></div>
<h2 class="abs soon-title">COMING SOON!</h2>
<p class="abs soon-sub">Get 1 on 1 PDH care on US for personalized remedies.</p>
<a class="abs btn btn-white" style="left:537px;top:2232px;width:125px;height:42px">GET STARTED</a>

<div class="abs perk" style="left:132px"><div class="check"><svg width="22" height="16" viewBox="0 0 22 16"><path d="M2 8l6 6L20 2" fill="none" stroke="#fff" stroke-width="3"/></svg></div><div class="label">LAB TEST PARTNERS</div></div>
<div class="abs perk" style="left:370px"><div class="check"><svg width="22" height="16" viewBox="0 0 22 16"><path d="M2 8l6 6L20 2" fill="none" stroke="#fff" stroke-width="3"/></svg></div><div class="label">UNLIMITED CLASSES</div></div>
<div class="abs perk" style="left:608px"><div class="check"><svg width="22" height="16" viewBox="0 0 22 16"><path d="M2 8l6 6L20 2" fill="none" stroke="#fff" stroke-width="3"/></svg></div><div class="label">UNLIMITED YOGO</div></div>
<div class="abs perk" style="left:846px"><div class="check"><svg width="22" height="16" viewBox="0 0 22 16"><path d="M2 8l6 6L20 2" fill="none" stroke="#fff" stroke-width="3"/></svg></div><div class="label">UNLIMITED MEDITATION</div></div>

</body>
</html>
```